Business Card Design Project

it should have the logo in one side
the other side

Name
Position
telephone
email

Target Market(s)

Business prospects and upscale Fashion shoppers

Industry/Entity Type

Business

Font styles to use
Serif
Sans Serif

Requirements
Must have
• very elegant, upscale, modern
Nice to have
• layering, embossed
Should not have
• Should not use any color OTHER THAN black, silver, white or purple

```html
<!DOCTYPE html>
<html lang="en">
<head>
<meta charset="UTF-8">
<title>Harwick Business Card</title>
<link rel="stylesheet" href="https://fonts.googleapis.com/css2?family=Exo+2:wght@500;600;700&display=swap">
<style>
  :root {
    --backdrop: #e8e7ea;
    --card-white: #ffffff;
    --silver-dark: #8d9198;
    --silver-light: #eef0f2;
    --silver-mid: #b8bcc2;
    --purple-deep: #4a2868;
    --purple: #6b3f94;
    --ink: #1e1e22;
    --shadow: rgba(30, 20, 45, 0.2);
  }
  * { margin: 0; padding: 0; box-sizing: border-box; }
  html, body {
    width: 1200px;
    height: 901px;
    overflow: hidden;
    background: var(--backdrop);
    font-family: "Exo 2", Arial, sans-serif;
  }
  .sheet {
    position: relative;
    width: 1200px;
    height: 901px;
    display: flex;
    flex-direction: column;
    align-items: center;
    justify-content: center;
    gap: 40px;
  }
  .card {
    position: relative;
    width: 700px;
    height: 400px;
    border-radius: 40px;
    overflow: hidden;
    background: var(--card-white);
    box-shadow: 0 14px 30px var(--shadow);
  }
  .card-art {
    position: absolute;
    inset: 0;
    width: 100%;
    height: 100%;
  }
  .brand {
    position: absolute;
    display: flex;
    align-items: center;
    gap: 14px;
    color: var(--ink);
    font-size: 30px;
    font-weight: 600;
    letter-spacing: 3px;
  }
  .brand-square {
    width: 44px;
    height: 44px;
    background: var(--purple);
  }
  .card-back .brand {
    left: 50%;
    top: 50%;
    transform: translate(-50%, -50%);
  }
  .card-front .brand {
    left: 70px;
    top: 66px;
  }
  .holder {
    position: absolute;
    left: 32px;
    top: 244px;
    color: var(--ink);
    transform: rotate(-4deg);
    transform-origin: left top;
  }
  .holder-name {
    font-size: 28px;
    font-weight: 600;
    letter-spacing: 1.5px;
    line-height: 32px;
  }
  .holder-role {
    font-size: 13px;
    font-weight: 500;
    letter-spacing: 1.5px;
    margin-top: 2px;
  }
  .contact {
    position: absolute;
    right: 30px;
    top: 250px;
    text-align: right;
    color: var(--ink);
    font-weight: 500;
    list-style: none;
  }
  .contact-address {
    font-size: 13px;
    line-height: 16px;
    margin-bottom: 8px;
  }
  .contact-line {
    display: flex;
    justify-content: flex-end;
    align-items: center;
    gap: 8px;
    font-size: 13px;
    line-height: 18px;
  }
  .contact-line svg {
    width: 13px;
    height: 13px;
    fill: none;
    stroke: var(--purple-deep);
    stroke-width: 1.6;
  }
</style>
</head>
<body>
<main class="sheet">

  <section class="card card-back" aria-label="Card back">
    <div class="brand">
      <span class="brand-square"></span>
      <span class="brand-name">HARWICK</span>
    </div>
  </section>

  <section class="card card-front" aria-label="Card front">
    <svg class="card-art" viewBox="0 0 700 400" preserveAspectRatio="none" aria-hidden="true">
      <defs>
        <linearGradient id="silverFill" x1="0" y1="0" x2="1" y2="0.5">
          <stop offset="0" stop-color="var(--silver-mid)"/>
          <stop offset="0.5" stop-color="var(--silver-light)"/>
          <stop offset="1" stop-color="var(--silver-dark)"/>
        </linearGradient>
      </defs>
      <path class="silver-band" d="M0,205 C140,160 280,215 420,215 C540,215 620,175 700,150 L700,400 L0,400 Z" fill="url(#silverFill)"/>
      <path class="accent-line" d="M0,190 C140,145 280,200 420,200 C540,200 620,160 700,135" fill="none" stroke="var(--purple-deep)" stroke-width="4"/>
      <path class="ribbon" d="M300,240 C430,205 560,180 690,200 C570,195 440,222 300,240 Z" fill="var(--purple-deep)"/>
      <path class="ribbon" d="M330,262 C460,230 580,208 690,226 C585,222 460,246 330,262 Z" fill="var(--purple)"/>
    </svg>

    <div class="brand">
      <span class="brand-square"></span>
      <span class="brand-name">HARWICK</span>
    </div>

    <div class="holder">
      <p class="holder-name">DANIEL REEVE</p>
      <p class="holder-role">MANAGING DIRECTOR</p>
    </div>

    <ul class="contact">
      <li class="contact-address">27, 9th floor, Crest Tower<br>Marlow Road NTW</li>
      <li class="contact-line">014 220 5371
        <svg viewBox="0 0 16 16"><path d="M4 2 L6 2 L7 5 L5.5 6.5 C6.5 8.5 7.5 9.5 9.5 10.5 L11 9 L14 10 L14 12 C14 13 13 14 12 14 C7 14 2 9 2 4 C2 3 3 2 4 2 Z"/></svg>
      </li>
      <li class="contact-line">014 220 5372
        <svg viewBox="0 0 16 16"><rect x="4.5" y="1.5" width="7" height="13" rx="1"/><line x1="7" y1="12" x2="9" y2="12"/></svg>
      </li>
      <li class="contact-line">014 220 5373
        <svg viewBox="0 0 16 16"><rect x="2" y="6" width="12" height="8"/><rect x="4.5" y="2" width="7" height="4"/></svg>
      </li>
      <li class="contact-line">daniel@harwickmail.com
        <svg viewBox="0 0 16 16"><rect x="1.5" y="3.5" width="13" height="9"/><path d="M1.5 3.5 L8 9 L14.5 3.5"/></svg>
      </li>
      <li class="contact-line">www.harwickstudio.com
        <svg viewBox="0 0 16 16"><circle cx="8" cy="8" r="6.5"/><line x1="1.5" y1="8" x2="14.5" y2="8"/><ellipse cx="8" cy="8" rx="3" ry="6.5"/></svg>
      </li>
    </ul>
  </section>

</main>
</body>
</html>
```